We are a doctors medical practice
I need the business card to be eye catching and memorable,
to reflect professionalism, yet also warmth and care

the numbers need to be easy to see, for the elderly

and the logo also in a location that is large enough to see and be eye catching

Back of card:
opening hours:
Mon- Fri 8.30am to 6pm
Sat 9am to 4pm

rows for appontments, date and time
Updates

HiĀ 

Modification to company name

BROOKVALE KINDRED HEALTH MEDICAL PRACTICE

Thanks
Marla

Reason: I am look for a unique design that also fulfils the design brief

I have attempted to post a .eps and .ai file of the logo

Target Market(s)

needs to appeal to the majority, mainly adults

Industry/Entity Type

Medical

Contact Information for Business Card

company name: Brookvale Kindred Health Medical Practice
Name: Dr Marla Vossberg-Tait
Qualifications: MBBS, Bsci(med), FRACGP, DCH, SH&FPA, Dip Derm
Address: Shop 3/41-43 Quorrow St, Brookvale 2940
Ph: 02 9418 3052
Fax: 02 9461 8824

Requirements
Nice to have
• I like balance
gold/ silver incorporated, as well as the other colours in the logo- but not limited to these colours
a "medical" feel
Should not have
• dark or strong colours

```html
<!DOCTYPE html>
<html lang="en">
<head>
<meta charset="utf-8">
<title>Brookvale Kindred Health Medical Practice – Business Card</title>
<link href="https://fonts.googleapis.com/css2?family=Montserrat:ital,wght@0,400;0,600;0,700;1,400&display=swap" rel="stylesheet">
<style>
  :root {
    --backdrop: #dcdcdc;
    --card: #ffffff;
    --brand-blue: #1a7cc4;
    --band-cyan: #4dc5de;
    --soft-blue: #dbe7f3;
    --faint-blue: #eef3f9;
    --text-grey: #7a7a7a;
    --rule-grey: #9a9a9a;
    --white: #ffffff;
    --qual-tint: #d9f3f9;
  }
  * { box-sizing: border-box; margin: 0; padding: 0; }
  html, body { width: 1200px; height: 1000px; overflow: hidden; }
  body {
    background: var(--backdrop);
    font-family: "Montserrat", Arial, sans-serif;
    position: relative;
  }
  .card {
    position: absolute;
    width: 507px;
    height: 306px;
    background: var(--card);
    overflow: hidden;
  }
  .card--front { left: 346px; top: 186px; }
  .card--back { left: 347px; top: 523px; }

  .front__backdrop-ring {
    position: absolute;
    left: 24px; top: -40px;
    width: 420px; height: 420px;
    border-radius: 50%;
    border: 36px solid var(--faint-blue);
  }
  .brand {
    position: absolute;
    left: 0; right: 0; top: 20px;
    text-align: center;
    color: var(--brand-blue);
    font-weight: 700;
  }
  .brand__mark {
    display: block;
    margin: 0 auto;
    width: 100px; height: 100px;
    border-radius: 50%;
    border: 6px solid var(--brand-blue);
    background: var(--card);
  }
  .brand__name {
    margin-top: 17px;
    font-size: 12.5px;
    letter-spacing: 0.2px;
  }
  .brand__rule {
    width: 190px;
    height: 1px;
    margin: 5px auto 5px;
    background: var(--band-cyan);
  }
  .brand__sub {
    font-size: 9.5px;
    letter-spacing: 1px;
  }
  .contact-band {
    position: absolute;
    left: 0; right: 0; bottom: 0;
    height: 110px;
    background: var(--band-cyan);
    color: var(--white);
    text-align: center;
  }
  .contact-band__name {
    margin-top: 11px;
    font-size: 14px;
    font-weight: 700;
    letter-spacing: 0.3px;
  }
  .contact-band__quals {
    margin-top: 1px;
    font-size: 8px;
    font-style: italic;
    color: var(--qual-tint);
  }
  .contact-band__address {
    margin-top: 12px;
    font-size: 13px;
  }
  .contact-band__phones {
    margin-top: 3px;
    font-size: 16px;
    font-weight: 700;
    letter-spacing: 0.3px;
  }

  .back__seal {
    position: absolute;
    left: 335px; top: 28px;
    width: 112px; height: 112px;
    border-radius: 50%;
    border: 6px solid var(--soft-blue);
  }
  .hours {
    position: absolute;
    left: 43px; top: 49px;
    color: var(--text-grey);
    font-size: 17px;
    line-height: 22px;
  }
  .hours__title { margin-bottom: 7px; }
  .appointment-row {
    position: absolute;
    left: 43px;
    width: 407px;
    color: var(--text-grey);
    font-size: 17px;
    padding-bottom: 4px;
    border-bottom: 1px dashed var(--rule-grey);
  }
  .appointment-row--date { top: 164px; }
  .appointment-row--time { top: 231px; }
</style>
</head>
<body>
  <section class="card card--front" aria-label="Business card front">
    <div class="front__backdrop-ring"></div>
    <div class="brand">
      <span class="brand__mark"></span>
      <div class="brand__name">BROOKVALE KINDRED HEALTH</div>
      <div class="brand__rule"></div>
      <div class="brand__sub">MEDICAL PRACTICE</div>
    </div>
    <div class="contact-band">
      <div class="contact-band__name">Dr MARLA VOSSBERG-TAIT</div>
      <div class="contact-band__quals">MBBS, Bsci(med), FRACGP, DCH, SH&amp;FPA, DipDerm</div>
      <div class="contact-band__address">Shop 3/41-43 Quorrow St, BROOKVALE 2940</div>
      <div class="contact-band__phones">T: 02 9418 3052 F: 02 9461 8824</div>
    </div>
  </section>

  <section class="card card--back" aria-label="Business card back">
    <div class="back__seal"></div>
    <div class="hours">
      <p class="hours__title">Opening Hours:</p>
      <p>Mon - Fri: 8.30am to 6pm</p>
      <p>Saturday: 9am to 4pm</p>
    </div>
    <div class="appointment-row appointment-row--date">Date:</div>
    <div class="appointment-row appointment-row--time">Time:</div>
  </section>
</body>
</html>
```